We are a all around maintence company for outdoor services. Commercial and residential: mowing, sprinkler repairs, power washing, parking lot striping, tree trimming, gutters cleaning, pond cleaning,feeding and fertilizing, flower bed clean up and fence repair.

Industry/Entity Type

It Company

Contact Information for Business Card

Bramblewick Yard Services
R.K. Mondavel
Cell 555-318-6047
P.O. Box 4518
Larkmoor,St 00000
Office 555-294-7730
Fax 555-294-7738

```html
<!DOCTYPE html>
<html lang="en">
<head>
<meta charset="utf-8">
<title>Bramblewick Yard Services – Business Card</title>
<link rel="stylesheet" href="https://fonts.googleapis.com/css2?family=Montserrat+Alternates:wght@600&family=Montserrat:wght@500&display=swap">
<style>
  :root {
    --page: #e9e6e1;
    --sky-top: #3fb0e8;
    --sky-bottom: #a6def7;
    --grass-light: #7cc843;
    --grass-dark: #4fa93a;
    --title: #ffffff;
    --title-edge: #1f3a4d;
    --ink: #14241a;
    --rule: #2e6a3a;
    --illustration-a: #8fbf5a;
    --illustration-b: #6b8f4a;
  }
  * { box-sizing: border-box; margin: 0; padding: 0; }
  html, body { width: 1200px; height: 806px; overflow: hidden; background: var(--page); }
  .sheet {
    width: 1200px; height: 806px;
    display: flex; flex-direction: column; align-items: center; justify-content: center; gap: 40px;
  }
  .card {
    position: relative; width: 680px; height: 340px; overflow: hidden;
    box-shadow: 0 6px 18px rgba(0,0,0,.18);
  }
  .card__scene { position: absolute; inset: 0; width: 100%; height: 100%; }
  .card__title {
    position: absolute; white-space: nowrap;
    font-family: "Montserrat Alternates", sans-serif; font-weight: 600;
    color: var(--title); letter-spacing: 1px; text-transform: uppercase;
    text-shadow: -1px -1px 0 var(--title-edge), 1px -1px 0 var(--title-edge),
                 -1px 1px 0 var(--title-edge), 1px 1px 0 var(--title-edge);
  }
  /* contact side */
  .contact .card__title { left: 30px; top: 26px; font-size: 27px; }
  .contact__rule { position: absolute; left: 30px; top: 68px; width: 520px; height: 1px; background: var(--rule); }
  .contact__list {
    position: absolute; left: 30px; top: 82px; list-style: none;
    font-family: "Montserrat", sans-serif; font-weight: 500; font-size: 21px; color: var(--ink);
  }
  .contact__item { display: flex; align-items: center; height: 29px; white-space: nowrap; }
  .contact__icon { width: 24px; height: 20px; margin-right: 12px; flex: none; }
  .contact__item--plain { padding-left: 36px; }
  /* front side */
  .front .card__title { right: 34px; top: 40px; font-size: 32px; }
  .front__illustration {
    position: absolute; left: 30px; top: 130px; width: 520px; height: 196px;
    border-radius: 14px;
    background: radial-gradient(ellipse at 50% 60%, var(--illustration-a), var(--illustration-b) 80%, transparent 100%);
    opacity: .85;
  }
</style>
</head>
<body>
<main class="sheet">

  <section class="card contact" aria-label="Card back with contact details">
    <svg class="card__scene" viewBox="0 0 680 340" preserveAspectRatio="none" aria-hidden="true">
      <defs>
        <linearGradient id="sky1" x1="0" y1="0" x2="0" y2="1">
          <stop offset="0" stop-color="var(--sky-top)"/><stop offset="1" stop-color="var(--sky-bottom)"/>
        </linearGradient>
        <linearGradient id="grass1" x1="0" y1="0" x2="1" y2="1">
          <stop offset="0" stop-color="var(--grass-dark)"/><stop offset="1" stop-color="var(--grass-light)"/>
        </linearGradient>
      </defs>
      <rect width="680" height="340" fill="url(#sky1)"/>
      <path d="M0 250 C150 220 260 120 420 95 C520 80 600 95 680 70 L680 340 L0 340 Z" fill="url(#grass1)"/>
    </svg>
    <h1 class="card__title">Bramblewick Yard Services</h1>
    <div class="contact__rule"></div>
    <ul class="contact__list">
      <li class="contact__item">
        <svg class="contact__icon" viewBox="0 0 24 20" fill="none" stroke="var(--ink)" stroke-width="1.5"><circle cx="12" cy="6" r="4"/><path d="M3 19c1-5 5-7 9-7s8 2 9 7z"/></svg>R.K. Mondavel</li>
      <li class="contact__item">
        <svg class="contact__icon" viewBox="0 0 24 20" fill="var(--ink)"><path d="M2 8c0-4 20-4 20 0v2h-5V8H7v2H2z"/><rect x="5" y="11" width="14" height="7" rx="2"/></svg>Cell 555-318-6047</li>
      <li class="contact__item">
        <svg class="contact__icon" viewBox="0 0 24 20" fill="var(--ink)"><rect x="2" y="6" width="5" height="13"/><rect x="8" y="9" width="14" height="10"/><rect x="10" y="2" width="10" height="6"/></svg>Fax 555-294-7738</li>
      <li class="contact__item">
        <svg class="contact__icon" viewBox="0 0 24 20" fill="none" stroke="var(--ink)" stroke-width="1.5"><rect x="2" y="4" width="20" height="13"/><path d="M2 4l10 8 10-8"/></svg>P.O. Box 4518</li>
      <li class="contact__item">
        <svg class="contact__icon" viewBox="0 0 24 20" fill="none" stroke="var(--ink)" stroke-width="1.5"><path d="M12 19s-6-6-6-10a6 6 0 0112 0c0 4-6 10-6 10z"/><circle cx="12" cy="9" r="2"/></svg>Larkmoor,St 00000</li>
      <li class="contact__item contact__item--plain">Office 555-294-7730</li>
    </ul>
  </section>

  <section class="card front" aria-label="Card front">
    <svg class="card__scene" viewBox="0 0 680 340" preserveAspectRatio="none" aria-hidden="true">
      <defs>
        <linearGradient id="sky2" x1="0" y1="0" x2="0" y2="1">
          <stop offset="0" stop-color="var(--sky-top)"/><stop offset="1" stop-color="var(--sky-bottom)"/>
        </linearGradient>
        <linearGradient id="grass2" x1="0" y1="0" x2="1" y2="1">
          <stop offset="0" stop-color="var(--grass-dark)"/><stop offset="1" stop-color="var(--grass-light)"/>
        </linearGradient>
      </defs>
      <rect width="680" height="340" fill="url(#sky2)"/>
      <path d="M0 200 C160 185 330 170 470 150 C560 135 620 110 680 90 L680 340 L0 340 Z" fill="url(#grass2)"/>
    </svg>
    <h2 class="card__title">Bramblewick Yard Services</h2>
    <div class="front__illustration" role="img" aria-label="Cartoon of a busy multi-armed groundskeeper sitting cross-legged with a laptop, phone and coffee, in front of a green picket fence, signpost, wheelbarrow and garden tools"></div>
  </section>

</main>
</body>
</html>
```